Craft brewery keg badge / badge branding to be on display on keg fonts in pubs and craft beer bars

We're a small craft beer producer and are looking to have a keg badge designed to be put onto keg fonts in bars as well as being used on our bottles. Our website is www.qlbrewery.co.uk. -Please take a look at our site however we're looking for new branding! We're not looking to have the windmill on the badge! We want a bold geometric hop design in the centre of the design. The beer is a low AVB beer (2.9% ABV) and will be hopped with Cascade, Colombus and Mosaic hops and will have a fruity / juicy aroma. We're looking to have a design that we can re-use again and again by changing: colours and wording for different beers in the future.

Target Market(s)
Craft beer drinkers
Industry/Entity Type
Craft Brewery
Requirements
Must have
- Simple, elegant, repeatable core message from the badge. It need a simple, bold geometric hop design (examples uploaded) in the centre which is repeatable across many brands in the future.
- The badge needs to be circular and 82mm across to fit our tap lenses (see http://www.velmo.co.uk/branding for the flat lens). The keg badge needs to be modern and in line with other keg badges like the examples attached- though we leave the artistic flair up to you guys. Please see below the styles of keg badge we like.
- Must be in vector file format and we must get a jpeg version too.

Should not have
- Should not be overcrowded and try to be too full of information. See attached examples.

```html
<!DOCTYPE html>
<html lang="en">
<head>
<meta charset="utf-8">
<title>Whetstone APA – Keg Badge Variants</title>
<link rel="stylesheet" href="https://fonts.googleapis.com/css2?family=Exo+2:wght@500;600;800&display=swap">
<style>
  :root {
    --page-bg: #fffdb6;
    --light-face-1: #f4ecc0;
    --light-face-2: #e6e7a4;
    --light-face-3: #b8bf82;
    --dark-face-1: #8f8754;
    --dark-face-2: #747424;
    --dark-face-3: #3f4a14;
    --hop-top: #f6ee4a;
    --hop-bottom: #f2b33c;
    --ink-dark: #111111;
    --ink-light: #ffffff;
  }
  * { margin: 0; padding: 0; box-sizing: border-box; }
  html, body {
    width: 1200px;
    height: 1200px;
    overflow: hidden;
    background: var(--page-bg);
  }
  .badge-sheet {
    position: relative;
    width: 1200px;
    height: 1200px;
  }
  .badge {
    position: absolute;
    width: 484px;
    height: 484px;
    font-family: "Exo 2", sans-serif;
  }
  .badge--top-left     { left: 49px;  top: 52px; }
  .badge--top-right    { left: 655px; top: 52px; }
  .badge--bottom-left  { left: 49px;  top: 652px; }
  .badge--bottom-right { left: 661px; top: 652px; }

  .badge__title   { font-weight: 800; font-size: 27px; }
  .badge__hops    { font-weight: 600; font-size: 12px; }
  .badge__brewery { font-weight: 600; font-size: 15px; letter-spacing: 0.2px; }
  .badge__abv     { font-weight: 600; font-size: 14px; }
  .badge__tagline { font-weight: 800; font-size: 16px; letter-spacing: 0.3px; }
  .badge__abv--small     { font-size: 11.5px; }
  .badge__tagline--flat  { font-weight: 600; font-size: 12px; letter-spacing: 0; }

  .badge--light text { fill: var(--ink-dark); }
  .badge--light .badge__rule { stroke: var(--ink-dark); }
  .badge--dark text { fill: var(--ink-light); }
  .badge--dark .badge__rule { stroke: var(--ink-light); }
</style>
</head>
<body>
<svg width="0" height="0" style="position:absolute" aria-hidden="true">
  <defs>
    <linearGradient id="face-light" x1="0" y1="0" x2="0.3" y2="1">
      <stop offset="0" style="stop-color: var(--light-face-1)"/>
      <stop offset="0.5" style="stop-color: var(--light-face-2)"/>
      <stop offset="1" style="stop-color: var(--light-face-3)"/>
    </linearGradient>
    <linearGradient id="face-dark" x1="0" y1="0" x2="0.3" y2="1">
      <stop offset="0" style="stop-color: var(--dark-face-1)"/>
      <stop offset="0.5" style="stop-color: var(--dark-face-2)"/>
      <stop offset="1" style="stop-color: var(--dark-face-3)"/>
    </linearGradient>
    <linearGradient id="hop-fill" x1="0" y1="0" x2="0" y2="1">
      <stop offset="0" style="stop-color: var(--hop-top)"/>
      <stop offset="1" style="stop-color: var(--hop-bottom)"/>
    </linearGradient>
    <path id="tagline-arc" d="M -160 152 A 250 250 0 0 0 160 152"/>
  </defs>
</svg>

<main class="badge-sheet">

  <svg class="badge badge--light badge--top-left" viewBox="-242 -242 484 484">
    <circle class="badge__face" r="242" fill="url(#face-light)" role="img" aria-label="Faceted geometric background in pale yellow and sage tones"/>
    <rect class="badge__hop" x="-100" y="-214" width="200" height="276" rx="40" fill="url(#hop-fill)" role="img" aria-label="Bold geometric hop cone illustration"/>
    <text class="badge__title" x="0" y="108" text-anchor="middle">Whetstone APA</text>
    <text class="badge__hops" x="0" y="126" text-anchor="middle">DDH APA; Cascade, Eureka, Columbus, and Vic Secret</text>
    <line class="badge__rule" x1="-155" y1="134" x2="155" y2="134" stroke-width="2"/>
    <text class="badge__brewery" x="0" y="154" text-anchor="middle">QUARRY LANE BREWING CO. LTD</text>
    <text class="badge__abv" x="0" y="185" text-anchor="middle">4.5% ABV</text>
    <text class="badge__tagline"><textPath href="#tagline-arc" startOffset="50%" text-anchor="middle">Undefined, Unfiltered and Vegan</textPath></text>
  </svg>

  <svg class="badge badge--dark badge--top-right" viewBox="-242 -242 484 484">
    <circle class="badge__face" r="242" fill="url(#face-dark)" role="img" aria-label="Faceted geometric background in olive and khaki tones"/>
    <rect class="badge__hop" x="-100" y="-214" width="200" height="276" rx="40" fill="url(#hop-fill)" role="img" aria-label="Bold geometric hop cone illustration"/>
    <text class="badge__title" x="0" y="108" text-anchor="middle">Whetstone APA</text>
    <text class="badge__hops" x="0" y="126" text-anchor="middle">DDH APA; Cascade, Eureka, Columbus, and Vic Secret</text>
    <line class="badge__rule" x1="-155" y1="134" x2="155" y2="134" stroke-width="2"/>
    <text class="badge__brewery" x="0" y="154" text-anchor="middle">QUARRY LANE BREWING CO. LTD</text>
    <text class="badge__abv" x="0" y="185" text-anchor="middle">4.5% ABV</text>
    <text class="badge__tagline"><textPath href="#tagline-arc" startOffset="50%" text-anchor="middle">Undefined, Unfiltered and Vegan</textPath></text>
  </svg>

  <svg class="badge badge--light badge--bottom-left" viewBox="-242 -242 484 484">
    <circle class="badge__face" r="242" fill="url(#face-light)" role="img" aria-label="Faceted geometric background in pale yellow and sage tones"/>
    <rect class="badge__hop" x="-100" y="-214" width="200" height="276" rx="40" fill="url(#hop-fill)" role="img" aria-label="Bold geometric hop cone illustration"/>
    <text class="badge__title" x="0" y="108" text-anchor="middle">Whetstone APA</text>
    <text class="badge__hops" x="0" y="126" text-anchor="middle">DDH APA; Cascade, Eureka, Columbus, and Vic Secret</text>
    <line class="badge__rule" x1="-155" y1="134" x2="155" y2="134" stroke-width="2"/>
    <text class="badge__brewery" x="0" y="154" text-anchor="middle">QUARRY LANE BREWING CO. LTD</text>
    <text class="badge__abv badge__abv--small" x="0" y="178" text-anchor="middle">4.5% ABV</text>
    <text class="badge__tagline badge__tagline--flat" x="0" y="204" text-anchor="middle">Undefined, Unfiltered and Vegan</text>
  </svg>

  <svg class="badge badge--dark badge--bottom-right" viewBox="-242 -242 484 484">
    <circle class="badge__face" r="242" fill="url(#face-dark)" role="img" aria-label="Faceted geometric background in olive and khaki tones"/>
    <rect class="badge__hop" x="-100" y="-214" width="200" height="276" rx="40" fill="url(#hop-fill)" role="img" aria-label="Bold geometric hop cone illustration"/>
    <text class="badge__title" x="0" y="108" text-anchor="middle">Whetstone APA</text>
    <text class="badge__hops" x="0" y="126" text-anchor="middle">DDH APA; Cascade, Eureka, Columbus, and Vic Secret</text>
    <line class="badge__rule" x1="-155" y1="134" x2="155" y2="134" stroke-width="2"/>
    <text class="badge__brewery" x="0" y="154" text-anchor="middle">QUARRY LANE BREWING CO. LTD</text>
    <text class="badge__abv badge__abv--small" x="0" y="178" text-anchor="middle">4.5% ABV</text>
    <text class="badge__tagline badge__tagline--flat" x="0" y="204" text-anchor="middle">Undefined, Unfiltered and Vegan</text>
  </svg>

</main>
</body>
</html>
```